photowall advertisement

We require a wall featuring our company logo. We would like to avoid the color green, and gold is highly preferred. The design should be similar to the one in the attached photo. The wall will be used for photos and promotional purposes during congresses. Files must be prepared for printing.
dimension of wall: 470x223 cm

Industry/Entity Type

lifestyle

Colors
0054AA
0677BA
7BADD7
CADEEF
E8F1F8
6B429C
8869AF
B7A5CE
E3DAEB
F3F0F8

Requirements
Must have
• gold color, white, and other compare with gold color
Nice to have
• some pictograms, maps of Europe

```html
<!DOCTYPE html>
<html lang="en">
<head>
<meta charset="utf-8">
<title>Nova Crest Studio – Photo Wall</title>
<link rel="stylesheet" href="https://fonts.googleapis.com/css2?family=Poppins:wght@600;700&display=swap">
<style>
  :root {
    --gold-deep: #fdb52a;
    --gold-light: #fdd68a;
    --gold-mid: #f0a535;
    --gold-warm: #ffc545;
    --bronze: #a0561c;
    --ink: #000000;
    --paper: #ffffff;
  }
  * { margin: 0; padding: 0; box-sizing: border-box; }
  html, body {
    width: 1200px;
    height: 566px;
    overflow: hidden;
    background: var(--paper);
  }
  .photo-wall {
    position: relative;
    width: 1200px;
    height: 566px;
    font-family: "Poppins", sans-serif;
  }
  .band {
    position: absolute;
    left: 0;
    width: 100%;
  }
  .band--gold {
    top: 0;
    height: 318px;
    background: linear-gradient(90deg,
      var(--gold-deep) 0%,
      var(--gold-deep) 8%,
      var(--gold-light) 26%,
      var(--gold-mid) 50%,
      var(--gold-light) 68%,
      var(--gold-warm) 88%,
      #e2a236 94%,
      var(--bronze) 100%);
    color: var(--ink);
  }
  .band--black {
    top: 318px;
    height: 248px;
    background: var(--ink);
    color: var(--paper);
  }
  .brand-mark {
    position: absolute;
    display: flex;
    align-items: center;
    gap: 10px;
    transform: translateY(-50%);
    white-space: nowrap;
  }
  .brand-mark__square {
    width: 24px;
    height: 24px;
    background: currentColor;
  }
  .brand-mark__name {
    font-weight: 700;
    font-size: 21px;
    letter-spacing: 1.5px;
    text-transform: uppercase;
  }
  .band--black .brand-mark__square { width: 22px; height: 22px; }
  .band--black .brand-mark__name { font-size: 19px; }
  .web-address {
    position: absolute;
    left: 0;
    width: 100%;
    top: 277px;
    text-align: center;
    font-weight: 700;
    font-size: 24px;
    color: var(--ink);
  }
</style>
</head>
<body>
  <main class="photo-wall">
    <section class="band band--gold">
      <div class="brand-mark" style="left:94px;top:40px"><span class="brand-mark__square"></span><span class="brand-mark__name">Nova Crest Studio</span></div>
      <div class="brand-mark" style="left:475px;top:40px"><span class="brand-mark__square"></span><span class="brand-mark__name">Nova Crest Studio</span></div>
      <div class="brand-mark" style="left:856px;top:40px"><span class="brand-mark__square"></span><span class="brand-mark__name">Nova Crest Studio</span></div>

      <div class="brand-mark" style="left:264px;top:103px"><span class="brand-mark__square"></span><span class="brand-mark__name">Nova Crest Studio</span></div>
      <div class="brand-mark" style="left:685px;top:103px"><span class="brand-mark__square"></span><span class="brand-mark__name">Nova Crest Studio</span></div>

      <div class="brand-mark" style="left:99px;top:166px"><span class="brand-mark__square"></span><span class="brand-mark__name">Nova Crest Studio</span></div>
      <div class="brand-mark" style="left:447px;top:166px"><span class="brand-mark__square"></span><span class="brand-mark__name">Nova Crest Studio</span></div>
      <div class="brand-mark" style="left:849px;top:166px"><span class="brand-mark__square"></span><span class="brand-mark__name">Nova Crest Studio</span></div>

      <div class="brand-mark" style="left:264px;top:235px"><span class="brand-mark__square"></span><span class="brand-mark__name">Nova Crest Studio</span></div>
      <div class="brand-mark" style="left:685px;top:235px"><span class="brand-mark__square"></span><span class="brand-mark__name">Nova Crest Studio</span></div>

      <p class="web-address">www.NovaCrestStudio.com</p>
    </section>

    <section class="band band--black">
      <div class="brand-mark" style="left:94px;top:39px"><span class="brand-mark__square"></span><span class="brand-mark__name">Nova Crest Studio</span></div>
      <div class="brand-mark" style="left:487px;top:39px"><span class="brand-mark__square"></span><span class="brand-mark__name">Nova Crest Studio</span></div>
      <div class="brand-mark" style="left:881px;top:39px"><span class="brand-mark__square"></span><span class="brand-mark__name">Nova Crest Studio</span></div>

      <div class="brand-mark" style="left:299px;top:96px"><span class="brand-mark__square"></span><span class="brand-mark__name">Nova Crest Studio</span></div>
      <div class="brand-mark" style="left:676px;top:96px"><span class="brand-mark__square"></span><span class="brand-mark__name">Nova Crest Studio</span></div>

      <div class="brand-mark" style="left:60px;top:149px"><span class="brand-mark__square"></span><span class="brand-mark__name">Nova Crest Studio</span></div>
      <div class="brand-mark" style="left:470px;top:159px"><span class="brand-mark__square"></span><span class="brand-mark__name">Nova Crest Studio</span></div>
      <div class="brand-mark" style="left:911px;top:149px"><span class="brand-mark__square"></span><span class="brand-mark__name">Nova Crest Studio</span></div>

      <div class="brand-mark" style="left:235px;top:205px"><span class="brand-mark__square"></span><span class="brand-mark__name">Nova Crest Studio</span></div>
      <div class="brand-mark" style="left:694px;top:205px"><span class="brand-mark__square"></span><span class="brand-mark__name">Nova Crest Studio</span></div>
    </section>
  </main>
</body>
</html>
```